PowerPoint Template Design for Management Consultancy

I need a PPT template for a new management consulting company. I want a modern look that uses dark blues and greys for divider slides, white content slides and a creative use of the logo in the slides. The supplied images are used on the website so I'd like to incorporate these into the theme

Target Market(s)

Management Consulting

Industry/Entity Type

Consulting

Font styles to use
Sans Serif

Colors
3277b5

Requirements
Must have
• Options for title slide, divider slides, content slides using the logo provided
Plain white content slides with creative use of logo
Color theme uses dark blues and greys
Nice to have
• Light and dark theme

```html
<!DOCTYPE html>
<html lang="en">
<head>
<meta charset="utf-8">
<title>Vantora Consulting – Presentation Template</title>
<link href="https://fonts.googleapis.com/css2?family=Poppins:wght@400;500;600;700;800&display=swap" rel="stylesheet">
<style>
:root{
  --navy:#14367c;
  --navy-deep:#1b2f5e;
  --header:#273f72;
  --ink:#1c2f5f;
  --grey:#7d7f86;
  --muted:#8a8d95;
  --line:#c9ccd3;
  --white:#ffffff;
  --page:#ffffff;
}
*{box-sizing:border-box;margin:0;padding:0}
html,body{width:1200px;height:3927px;overflow:hidden;background:var(--page)}
body{position:relative;font-family:'Poppins',sans-serif;color:var(--ink)}
.slide{position:absolute;left:69px;width:1062px;height:599px;background:var(--white);box-shadow:0 2px 10px rgba(0,0,0,.22);overflow:hidden}
.page-no{position:absolute;right:26px;font-weight:700;font-size:22px;color:var(--white)}
.brand{font-weight:700;color:var(--ink);letter-spacing:3px;text-align:center}
.brand-lg{position:absolute;left:0;right:0;font-size:64px;line-height:1}
.brand-sm{position:absolute;right:14px;bottom:12px;font-size:24px;letter-spacing:1.5px;line-height:1}
.band{position:absolute;left:0;right:0;background:var(--navy);color:var(--white);text-align:center;font-weight:700}
.header{position:absolute;left:0;top:0;width:100%;height:244px;background:linear-gradient(120deg,#22396a 0%,#2c4679 45%,#233a6c 100%);color:var(--white);text-align:center}
.header.process{background:linear-gradient(180deg,#4a5a72 0%,#5d6c80 40%,#2d3d5c 100%)}
.header h2{position:absolute;left:0;right:0;top:72px;font-size:50px;font-weight:800;letter-spacing:1px;line-height:1}
.header p{position:absolute;left:0;right:0;top:138px;font-size:13.5px;font-weight:500}
.header .page-no{top:14px}
.body-text{font-size:9.5px;line-height:17px;color:var(--grey)}
/* slide 2 */
.about{position:absolute;left:72px;top:325px;width:390px;padding-left:12px;border-left:3px solid var(--grey)}
.about small{display:block;font-size:13px;font-weight:500;color:var(--ink)}
.about h3{font-size:19px;font-weight:600;margin:2px 0 10px}
.point{position:absolute;left:538px;width:440px}
.point .num{position:absolute;left:0;top:0;width:48px;height:48px;background:var(--navy-deep);color:var(--white);font-size:21px;font-weight:600;display:flex;align-items:center;justify-content:center}
.point h4{margin-left:69px;font-size:14px;font-weight:600}
.point .body-text{margin-left:69px;margin-top:6px}
/* slide 3 */
.service{position:absolute;top:355px;width:320px}
.service .icon{position:absolute;left:0;top:6px;width:88px;height:88px}
.service h4{margin-left:109px;font-size:14px;font-weight:600}
.service .body-text{margin-left:109px;margin-top:6px;width:180px}
/* slide 4 */
.member{position:absolute;top:235px;width:209px;height:277px;background:var(--white);box-shadow:0 1px 6px rgba(0,0,0,.2);text-align:center}
.member .photo{height:137px;background:linear-gradient(180deg,#b9b4ae,#6f6a66)}
.member h4{font-size:14px;font-weight:500;margin:12px 0 4px}
.member .body-text{padding:0 16px;line-height:17px}
/* slide 5 */
.step{position:absolute;top:316px;width:220px;text-align:center}
.step .circle{margin:0 auto;width:106px;height:106px;border-radius:50%;background:var(--navy-deep);box-shadow:0 0 0 4px var(--white),0 0 0 6px var(--navy-deep);color:var(--white);font-size:46px;font-weight:700;display:flex;align-items:center;justify-content:center}
.step h4{font-size:13px;font-weight:600;margin:17px 0 6px}
.chevron{position:absolute;top:341px;width:52px;height:58px}
/* slide 6 */
.scene{position:absolute;left:0;top:0;width:100%;height:358px;background:linear-gradient(180deg,#f7f3ee 0%,#ece8e4 55%,#b9c4d2 100%)}
</style>
</head>
<body>

<!-- Title -->
<section class="slide" style="top:69px">
  <div class="brand brand-lg" style="top:140px">VANTORA CONSULTING</div>
  <div class="band" style="top:360px;height:239px">
    <div style="position:absolute;left:0;right:0;top:58px;font-size:29px;line-height:44px">Neque porro quisquam<br>est qui dolorem<br>2021</div>
    <span class="page-no" style="top:188px">01</span>
  </div>
</section>

<!-- About -->
<section class="slide" style="top:689px">
  <header class="header" role="img" aria-label="Navy-tinted office photo of a desk with laptop and papers">
    <span class="page-no">02</span>
    <h2>Little About Us</h2>
    <p>Neque porro quisquam est qui dolorem ipsum quia dolor sit amet, consectetur, adipisci velit...</p>
  </header>
  <div class="about">
    <small>About</small>
    <h3>Vantora Consulting</h3>
    <p class="body-text">Lorem ipsum is simply dummy text of the printing and typesetting industry. Lorem ipsum has been the industry's standard dummy text ever since the 1500s, when an unknown printer took a galley of type and scrambled it to make a type specimen book. It has survived not only five centuries, but also the leap into electronic typesetting, remaining essentially unchanged. It was popularised in the 1960s with the release of Letraset sheets containing Lorem ipsum passages, and more recently with desktop publishing software including versions of Lorem ipsum.</p>
  </div>
  <div class="point" style="top:293px"><div class="num">01</div><h4>Contrary to popular belief</h4><p class="body-text">Lorem ipsum is simply dummy text of the printing and<br>typesetting industry. Lorem ipsum has been the industry's<br>standard dummy text ever since the 1500s</p></div>
  <div class="point" style="top:383px"><div class="num">02</div><h4>Contrary to popular belief</h4><p class="body-text">Lorem ipsum is simply dummy text of the printing and<br>typesetting industry. Lorem ipsum has been the industry's<br>standard dummy text ever since the 1500s</p></div>
  <div class="point" style="top:473px"><div class="num">03</div><h4>Contrary to popular belief</h4><p class="body-text">Lorem ipsum is simply dummy text of the printing and<br>typesetting industry. Lorem ipsum has been the industry's<br>standard dummy text ever since the 1500s</p></div>
  <div class="brand brand-sm">VANTORA</div>
</section>

<!-- Services -->
<section class="slide" style="top:1323px">
  <header class="header" role="img" aria-label="Navy-tinted office photo of a desk with laptop and papers">
    <span class="page-no">03</span>
    <h2>What We Do</h2>
    <p>Neque porro quisquam est qui dolorem ipsum quia dolor sit amet, consectetur, adipisci velit...</p>
  </header>
  <div class="service" style="left:57px">
    <svg class="icon" viewBox="0 0 88 88"><circle cx="44" cy="44" r="43" fill="none" stroke="#1b2f5e" stroke-width="1.5"/><circle cx="44" cy="44" r="38" fill="#1b2f5e"/><g fill="none" stroke="#fff" stroke-width="2"><path d="M33 28h17l7 7v25H33z"/><path d="M50 28v7h7"/><path d="M38 40h14M38 45h14M38 50h14M38 55h10"/></g></svg>
    <h4>Contrary to popular</h4><p class="body-text">Lorem ipsum is simply dummy text of the printing and typesetting industry. Lorem ipsum has been the industry's standard dummy text ever since the 1500s</p>
  </div>
  <div class="service" style="left:392px">
    <svg class="icon" viewBox="0 0 88 88"><circle cx="44" cy="44" r="43" fill="none" stroke="#1b2f5e" stroke-width="1.5"/><circle cx="44" cy="44" r="38" fill="#1b2f5e"/><g fill="none" stroke="#fff" stroke-width="2"><circle cx="44" cy="38" r="8"/><path d="M29 59c0-9 7-13 15-13s15 4 15 13z"/></g></svg>
    <h4>Contrary to popular</h4><p class="body-text">Lorem ipsum is simply dummy text of the printing and typesetting industry. Lorem ipsum has been the industry's standard dummy text ever since the 1500s</p>
  </div>
  <div class="service" style="left:727px">
    <svg class="icon" viewBox="0 0 88 88"><circle cx="44" cy="44" r="43" fill="none" stroke="#1b2f5e" stroke-width="1.5"/><circle cx="44" cy="44" r="38" fill="#1b2f5e"/><g fill="none" stroke="#fff" stroke-width="2" stroke-linejoin="round"><path d="M27 44l33-14-8 30-9-9z"/><path d="M60 30L43 51v9l5-6"/></g></svg>
    <h4>Contrary to popular</h4><p class="body-text">Lorem ipsum is simply dummy text of the printing and typesetting industry. Lorem ipsum has been the industry's standard dummy text ever since the 1500s</p>
  </div>
  <div class="brand brand-sm">VANTORA</div>
</section>

<!-- Team -->
<section class="slide" style="top:1968px">
  <header class="header" role="img" aria-label="Navy-tinted photo of a smiling professional">
    <span class="page-no">04</span>
    <h2 style="left:75px">Meet Our Team</h2>
    <p>Neque porro quisquam est qui dolorem ipsum quia dolor sit amet, consectetur, adipisci velit...</p>
  </header>
  <div class="member" style="left:99px"><div class="photo" role="img" aria-label="Portrait photo of team member in shirt and tie"></div><h4>Daniel R Whitfield</h4><p class="body-text">Lorem ipsum is simply dummy text of the printing and typesetting industry. Lorem ipsum has been the industry's standard dummy text ever since the 1500s</p></div>
  <div class="member" style="left:317px"><div class="photo" role="img" aria-label="Portrait photo of team member in light cardigan" style="background:linear-gradient(180deg,#e4ded6,#b8aea4)"></div><h4>Elena K Marsh</h4><p class="body-text">Lorem ipsum is simply dummy text of the printing and typesetting industry. Lorem ipsum has been the industry's standard dummy text ever since the 1500s</p></div>
  <div class="member" style="left:535px"><div class="photo" role="img" aria-label="Portrait photo of team member in navy sweater" style="background:linear-gradient(180deg,#d9d2c8,#2b3550)"></div><h4>Owen L Prescott</h4><p class="body-text">Lorem ipsum is simply dummy text of the printing and typesetting industry. Lorem ipsum has been the industry's standard dummy text ever since the 1500s</p></div>
  <div class="member" style="left:753px"><div class="photo" role="img" aria-label="Portrait photo of team member holding a tablet" style="background:linear-gradient(180deg,#b08a5e,#5e4a3a)"></div><h4>Claire N Dalton</h4><p class="body-text">Lorem ipsum is simply dummy text of the printing and typesetting industry. Lorem ipsum has been the industry's standard dummy text ever since the 1500s</p></div>
  <div class="brand brand-sm">VANTORA</div>
</section>

<!-- Process -->
<section class="slide" style="top:2613px">
  <header class="header process" role="img" aria-label="Photo of two hikers celebrating on a misty mountain ridge">
    <span class="page-no">05</span>
    <h2>Step Process</h2>
    <p>Neque porro quisquam est qui dolorem ipsum quia dolor sit amet, consectetur, adipisci velit...</p>
  </header>
  <div class="step" style="left:135px"><div class="circle">01</div><h4>Neque porro quisquam</h4><p class="body-text">Lorem ipsum is simply dummy text of the<br>printing and typesetting industry. Lorem<br>ipsum has been the industry's standard<br>dummy text ever since the 1500s,</p></div>
  <svg class="chevron" style="left:357px" viewBox="0 0 52 58"><path d="M2 2h16l30 27-30 27H2l30-27z" fill="none" stroke="#1b2f5e" stroke-width="1.8" stroke-linejoin="round"/></svg>
  <div class="step" style="left:402px"><div class="circle">02</div><h4>Neque porro quisquam</h4><p class="body-text">Lorem ipsum is simply dummy text of the<br>printing and typesetting industry. Lorem<br>ipsum has been the industry's standard<br>dummy text ever since the 1500s,</p></div>
  <svg class="chevron" style="left:625px" viewBox="0 0 52 58"><path d="M2 2h16l30 27-30 27H2l30-27z" fill="none" stroke="#1b2f5e" stroke-width="1.8" stroke-linejoin="round"/></svg>
  <div class="step" style="left:709px"><div class="circle">03</div><h4>Neque porro quisquam</h4><p class="body-text">Lorem ipsum is simply dummy text of the<br>printing and typesetting industry. Lorem<br>ipsum has been the industry's standard<br>dummy text ever since the 1500s,</p></div>
  <div class="brand brand-sm">VANTORA</div>
</section>

<!-- Contact -->
<section class="slide" style="top:3258px">
  <div class="scene" role="img" aria-label="Soft photo of climbers helping each other up a cliff above hazy blue mountains"></div>
  <div class="brand brand-lg" style="top:140px">VANTORA CONSULTING</div>
  <div class="band" style="top:358px;height:241px">
    <div style="position:absolute;left:0;right:0;top:74px;font-size:29px;line-height:52px">Phone: +0198 765 432<br>Mail: hello@vantora.example</div>
    <span class="page-no" style="top:192px">06</span>
  </div>
</section>

</body>
</html>
```